Flyer Design for Business: "Velvet Dune"

My Business name is "VELVET DUNE"

Laser Hair Removal
Non invasive and pain free
Look amazing and feel confident with a Hair Free body
Now is the time to start don't delay
1 treatment a month will ensure you are bikini hot for the summer months
Take full advantage of our OPENING SPECIALS of 30%-40% savings
Part payments available

CELLULITE & FAT REDUCTION
Now you too can look amazing without invasive surgery, downtime or discomfort
Lorna Pettigrew & Beatrix Holloway are avid recipients of this treatment.
Effective on all skin types and delivers fast measurable results for:
Helping mums regain their pre-baby figures
Losing the love handles (but keeping the love)
Stretch mark reduction
Skin tightening
Cellulite busting on Arms, tummy, thighs.
Man boob reduction.
Latest technology:
Bi Polar radio frequency (RF)
infrared light
negative pressure (Vacuum)
Tissue manipulation through roller mechanical massage.
50% saving Call now

PDT LED REJUVENATION LIGHT THERAPY
KOTR Researchers found:
Fibroblast and muscles grew 5 times faster, stimulates
reconstruction of collagenous fibres of the dermis
These findings and more assist with:
Remove freckles, sunburn pigmentation,
Cures acne and hair follicle inflammation
Anti aging skin tightening
Reduces pore size
Improve the skin texture
Improves circulation
Red light : reduces pore size, softens skin wrinkles,reduces acne
Blue light: Kills the acne bacillus to eliminate acne, inhibit inflammation
Yellow light: Skin tightening, whitening and softens skin wrinkles
Purple light: combination of red & blue lights treats acne scars
Orange light increases cell energy and accelerates metabolism
$55 Saving and relax under the lights.

Who can resist a soothing Hot stone massage therapy after:
A hard stressful day at work
Aches and muscular pain

Pick anything from this info with a couple of nice images.

Target Market(s)

Females & males Sports minded people cyclists

Industry/Entity Type

Beauty Salon

Colors
00a990
e34197

Requirements
Must have
• a couple of images and
Nice to have
• Pink and bluey green like my business card

```html
<!DOCTYPE html>
<html lang="en">
<head>
<meta charset="utf-8">
<title>Velvet Dune – Flyer</title>
<link href="https://fonts.googleapis.com/css2?family=Open+Sans:wght@400;600;700&family=Raleway:wght@300&family=Roboto+Condensed:wght@700&family=Great+Vibes&display=swap" rel="stylesheet">
<style>
  :root {
    --pink: #e34197;
    --teal: #00a990;
    --text: #3a3a3a;
    --grey: #777;
    --white: #ffffff;
    --skin-light: #f6e6dc;
    --skin-mid: #e9c8b5;
  }
  * { margin: 0; padding: 0; box-sizing: border-box; }
  html, body { width: 848px; height: 1200px; overflow: hidden; background: var(--white); }
  .flyer { position: relative; width: 848px; height: 1200px; font-family: "Open Sans", Arial, sans-serif; color: var(--text); }

  .hero-photo {
    position: absolute; left: 0; top: 0; width: 340px; height: 820px;
    background: radial-gradient(ellipse 60% 55% at 35% 45%, var(--skin-mid) 0%, var(--skin-light) 55%, var(--white) 100%);
  }

  .brand { position: absolute; left: 560px; top: 110px; width: 250px; text-align: center; }
  .brand-name { font-family: "Great Vibes", cursive; font-size: 44px; color: var(--pink); line-height: 1; }
  .brand-tag { font-size: 11px; color: var(--grey); letter-spacing: 0.5px; margin-top: 12px; }

  .headline {
    position: absolute; left: 332px; top: 180px;
    font-family: "Raleway", Arial, sans-serif; font-weight: 300;
    font-size: 55px; line-height: 62px; color: #2c2c2c;
  }

  .services { position: absolute; left: 336px; top: 327px; font-size: 12.3px; line-height: 18.3px; white-space: nowrap; }
  .services h2 { font-size: 14px; color: var(--pink); font-weight: 700; line-height: 19px; }
  .services .sub-pink { color: var(--pink); font-weight: 700; }
  .services .sub-teal { color: var(--teal); font-weight: 700; }
  .services .gap { margin-top: 18px; }
  .services b { font-weight: 700; }

  .thumb { position: absolute; border-radius: 50%; border: 3px solid var(--pink); }
  .thumb.teal { border-color: var(--teal); }
  .thumb-massage { left: 684px; top: 294px; width: 136px; height: 136px; background: radial-gradient(circle at 45% 45%, #eed5c8, #b9c2cc); }
  .thumb-laser { left: 612px; top: 442px; width: 164px; height: 164px; background: radial-gradient(circle at 50% 50%, #f3e1d6, #e7e7ea); }
  .thumb-waist { left: 678px; top: 622px; width: 120px; height: 120px; background: radial-gradient(circle at 50% 45%, #e4b79f, #d54f4f 70%, #6e8db0); }
  .thumb-chest { left: 640px; top: 752px; width: 144px; height: 144px; background: radial-gradient(circle at 40% 50%, #f0c9b0, #e0a98d); }
  .thumb-facial { left: 698px; top: 990px; width: 124px; height: 124px; background: radial-gradient(circle at 50% 50%, #eadfe0, #9fb9c8); }

  .offer {
    position: absolute; left: 0; top: 805px; width: 322px; height: 154px;
    background: var(--pink); border-top-right-radius: 55px;
    font-family: "Roboto Condensed", Arial, sans-serif; font-weight: 700;
    color: var(--white); text-align: center; padding-top: 25px;
  }
  .offer p { font-size: 19px; line-height: 30px; }
  .offer .offer-big { font-size: 24px; line-height: 30px; }

  .benefits {
    position: absolute; left: 0; top: 959px; width: 322px; height: 166px;
    background: var(--teal); color: var(--white);
    font-size: 13.4px; font-weight: 700; line-height: 20.3px;
    padding: 26px 0 0 30px; list-style: none;
  }
  .benefits li { padding-left: 12px; text-indent: -12px; }
  .benefits li::before { content: "• "; }

  .footer { position: absolute; left: 0; top: 1135px; width: 848px; text-align: center; }
  .footer-contact { font-size: 15px; font-weight: 700; color: #333; }
  .footer-address { font-size: 13px; color: #333; margin-top: 2px; }
  .footer-address b { font-weight: 700; }
</style>
</head>
<body>
<main class="flyer">
  <div class="hero-photo" role="img" aria-label="Photo of a woman seated with knees drawn up, smooth bare skin"></div>

  <header class="brand">
    <div class="brand-name">Velvet Dune</div>
    <div class="brand-tag">Laser Hair Removal</div>
  </header>

  <h1 class="headline">Let's get<br>Gorgeous!</h1>

  <section class="services">
    <h2>CELLULITE &amp; FAT REDUCTION</h2>
    <p>Now you too can look amazing without invasive surgery,<br>downtime or discomfort Lorna Pettigrew &amp; Beatrix<br>Holloway are avid recipients of this treatment.</p>
    <p class="sub-teal">Effective on all skin types and<br>delivers fast measurable results for:</p>
    <p>Helping mums regain their pre-baby figures<br>Losing the love handles (but keeping the love)<br>Stretch mark reduction<br>Skin tightening<br>Cellulite busting on Arms, tummy, thighs.<br>Man boob reduction.</p>
    <p class="sub-teal gap">Latest technology:</p>
    <p>Bi Polar radio frequency (RF)<br>infrared light<br>negative pressure (Vacuum)<br>Tissue manipulation through roller<br>mechanical massage.<br>50% saving Call now</p>

    <h2 class="gap">PDT LED REJUVENATION LIGHT THERAPY</h2>
    <p class="sub-pink">KOTR Researchers found:</p>
    <p>Fibroblast and muscles grew 5 times faster, stimulates<br>reconstruction of collagenous fibres of the dermis</p>
    <p class="sub-pink gap">These findings and more assist with:</p>
    <p>Remove freckles, sunburn pigmentation,<br>Cures acne and hair follicle inflammation<br>Anti aging skin tightening<br>Reduces pore size<br>Improve the skin texture<br>Improves circulation<br>
    <b>Red light:</b> reduces pore size, softens skin wrinkles,reduces acne<br>
    <b>Blue light:</b> Kills the acne bacillus to eliminate acne, inhibit inflammation<br>
    <b>Yellow light:</b> Skin tightening, whitening and softens skin wrinkles<br>
    <b>Purple light:</b> combination of red &amp; blue lights treats acne scars<br>
    Orange light increases cell energy and accelerates metabolism<br>
    $55 Saving and relax under the lights.</p>
    <p class="gap">Who can resist a soothing Hot stone massage therapy after:<br>A hard stressful day at work<br>Aches and muscular pain</p>
  </section>

  <div class="thumb thumb-massage" role="img" aria-label="Back massage treatment photo"></div>
  <div class="thumb teal thumb-laser" role="img" aria-label="Underarm laser hair removal photo"></div>
  <div class="thumb thumb-waist" role="img" aria-label="Slim waist in oversized jeans photo"></div>
  <div class="thumb thumb-chest" role="img" aria-label="Close-up of chest skin photo"></div>
  <div class="thumb teal thumb-facial" role="img" aria-label="Facial light therapy treatment photo"></div>

  <aside class="offer">
    <p>Take full advantage of our</p>
    <p>OPENING SPECIALS of</p>
    <p class="offer-big">30%-40% savings</p>
    <p>Part payments available</p>
  </aside>

  <ul class="benefits">
    <li>Non invasive and pain free</li>
    <li>Look amazing and feel confident<br>with a Hair Free body</li>
    <li>Now is the time to start don't delay<br>1 treatment a month will ensure you<br>are bikini hot for the summer months</li>
  </ul>

  <footer class="footer">
    <p class="footer-contact">For all appointments call:&nbsp; (02) 5550 1472 | email:&nbsp; info@velvetdune.com.au | www.velvetdune.com.au</p>
    <p class="footer-address"><b>Velvet Dune,</b> Medical Aesthetician: Marama Tane, 4/18 Harbour Lane, Wattle Grove NSW 2170.</p>
  </footer>
</main>
</body>
</html>
```